Business Card & Stationary
For Event Planning Website
I need single sided standard sized Business Card [3.5" x 2"]
Same as logo or similar
Professional
First Name Last Name
Founder & Chief Executive Officer
Address 1
Address 2
New York, NY 10016
xyz@juniperhours.com
www.juniperhours.com
Feel free to be creative - the site is for party planning (weddings, bar-mitzvahs, etc.) so it should be modern & professional, with a fun factor.
I used test data to protect personal data but I can supply you with all of the information you need later.
I'm not sure which eps file corresponds to the jpg.
This is the hamsa (hand) which is part of the logo
The hand - ai file
Webpage Background Pattern

```html
<!DOCTYPE html>
<html lang="en">
<head>
<meta charset="utf-8">
<title>JuniperHours Stationery</title>
<link href="https://fonts.googleapis.com/css2?family=Roboto:wght@300;400;500&display=swap" rel="stylesheet">
<style>
  :root {
    --backdrop: #d6d6d6;
    --paper: #ffffff;
    --blue-deep: #1581cc;
    --blue-mid: #1f98de;
    --blue-light: #56c6f4;
    --ink-blue: #1f8fd6;
    --ink-grey: #6d7a86;
    --shadow: rgba(0,0,0,0.18);
  }
  * { margin: 0; padding: 0; box-sizing: border-box; }
  html, body { width: 1200px; height: 881px; overflow: hidden; }
  body {
    background: var(--backdrop);
    font-family: "Roboto", Arial, sans-serif;
    position: relative;
  }
  .sheet {
    position: absolute;
    background: var(--paper);
    box-shadow: 0 1px 4px var(--shadow);
  }
  .band {
    position: absolute;
    left: 0; right: 0;
    background: linear-gradient(90deg, var(--blue-deep) 0%, var(--blue-mid) 45%, var(--blue-light) 75%, var(--blue-mid) 100%);
  }
  .rule {
    position: absolute;
    left: 0; right: 0;
    height: 3px;
    background: var(--blue-mid);
  }
  .brand {
    position: absolute;
    color: #fff;
    font-weight: 400;
    letter-spacing: -0.3px;
    white-space: nowrap;
  }
  .brand-dot {
    position: absolute;
    border-radius: 50%;
    border: 2px solid var(--ink-blue);
  }
  .small-print {
    position: absolute;
    color: var(--ink-blue);
    font-size: 5.5px;
    line-height: 7.5px;
  }

  /* Letterhead */
  .letterhead { left: 38px; top: 36px; width: 528px; height: 809px; }
  .letterhead .rule { top: 12px; }
  .letterhead .band { top: 18px; height: 24px; }
  .letterhead .brand { right: 10px; top: 20px; font-size: 18px; }
  .letterhead .brand-dot { right: 26px; top: 48px; width: 12px; height: 12px; }
  .letterhead .small-print { left: 0; right: 0; bottom: 12px; text-align: center; }

  /* Business card */
  .business-card { left: 598px; top: 36px; width: 201px; height: 130px; border-radius: 10px; overflow: hidden; }
  .business-card .band { top: 0; height: 42px; }
  .business-card .brand { right: 8px; top: 6px; font-size: 14px; }
  .card-name {
    position: absolute; left: 0; right: 0; top: 42px; height: 20px;
    padding: 3px 8px; background: #f3f8fc;
    color: var(--ink-blue); font-size: 7px; line-height: 7px;
  }
  .card-name .title { font-size: 4.5px; line-height: 6px; color: var(--ink-grey); }
  .card-address { left: 8px; top: 74px; }
  .card-contact { right: 8px; top: 74px; text-align: right; }

  /* Letter envelope, front */
  .envelope-front { left: 598px; top: 209px; width: 561px; height: 300px; }
  .envelope-front .rule { top: 14px; }
  .envelope-front .band { top: 21px; height: 20px; }
  .envelope-front .brand { right: 10px; top: 22px; font-size: 16px; }
  .envelope-front .brand-dot { right: 24px; top: 46px; width: 10px; height: 10px; }
  .envelope-front .small-print { left: 10px; bottom: 10px; }

  /* Envelope, back */
  .envelope-back { left: 598px; top: 547px; width: 561px; height: 298px; }
  .envelope-back svg { position: absolute; left: 0; top: 0; }
</style>
</head>
<body>

  <section class="sheet letterhead" aria-label="Letterhead">
    <div class="rule"></div>
    <div class="band"></div>
    <div class="brand">JuniperHours</div>
    <div class="brand-dot"></div>
    <div class="small-print">
      Address 1 | Address 2<br>
      New York, NY 10016<br>
      Phone (212) 555-0148 | Email: xyz@juniperhours.com | www.juniperhours.com
    </div>
  </section>

  <section class="sheet business-card" aria-label="Business card">
    <div class="band"></div>
    <div class="brand">JuniperHours</div>
    <div class="card-name">
      First Name Last Name
      <div class="title">Founder &amp; Chief Executive Officer</div>
    </div>
    <div class="small-print card-address">
      Address 1<br>Address 2<br>New York, NY 10016
    </div>
    <div class="small-print card-contact">
      Phone (212) 555-0148<br>Email: xyz@juniperhours.com<br>www.juniperhours.com
    </div>
  </section>

  <section class="sheet envelope-front" aria-label="Envelope front">
    <div class="rule"></div>
    <div class="band"></div>
    <div class="brand">JuniperHours</div>
    <div class="brand-dot"></div>
    <div class="small-print">
      Address 1<br>Address 2<br>New York, NY 10016<br>
      Phone (212) 555-0148 | Email: xyz@juniperhours.com | www.juniperhours.com
    </div>
  </section>

  <section class="sheet envelope-back" aria-label="Envelope back">
    <svg width="561" height="90" viewBox="0 0 561 90">
      <defs>
        <linearGradient id="flap-fill" x1="0" y1="0" x2="1" y2="0">
          <stop offset="0" stop-color="#1581cc"/>
          <stop offset="0.5" stop-color="#56c6f4"/>
          <stop offset="1" stop-color="#1581cc"/>
        </linearGradient>
      </defs>
      <path d="M0 0 H561 V8 Q556 82 530 82 H31 Q5 82 0 8 Z" fill="url(#flap-fill)"/>
      <circle cx="280.5" cy="42" r="11" fill="none" stroke="#ffffff" stroke-width="2"/>
    </svg>
  </section>

</body>
</html>
```